Business Card Design

Design new business card using new logo attached and some details as old business card, which is also attached.

Industry/Entity Type

Business

```html
<!DOCTYPE html>
<html lang="en">
<head>
<meta charset="utf-8">
<title>Business Card – Daniel Whitford, CPA, PA</title>
<link rel="stylesheet" href="https://fonts.googleapis.com/css2?family=Jost:wght@400;500&display=swap">
<style>
  :root {
    --page-bg: #d9dadd;
    --card-white: #ffffff;
    --curve-shade: #e4e5e8;
    --card-dark-center: #3b3e4b;
    --card-dark-edge: #15161c;
    --name-ink: #ececf0;
    --tagline-ink: #a8aab6;
    --contact-ink: #e6e7eb;
    --divider: #4a4d5a;
    --brand-ink: #2c2a4c;
    --web-ink: #8d8f9a;
  }
  html, body {
    margin: 0;
    width: 1200px;
    height: 1000px;
    overflow: hidden;
    background: var(--page-bg);
  }
  .canvas {
    position: relative;
    width: 1200px;
    height: 1000px;
    font-family: "Jost", "Helvetica Neue", Arial, sans-serif;
  }
  .business-card {
    position: absolute;
    left: 216px;
    top: 74px;
    width: 784px;
    height: 470px;
    overflow: hidden;
    background: var(--card-white);
    box-shadow: 0 6px 14px rgba(0,0,0,0.28);
  }
  .card-shape {
    position: absolute;
    inset: 0;
  }
  .brand-block {
    position: absolute;
    left: 14px;
    top: 214px;
    width: 244px;
    text-align: center;
  }
  .brand-name {
    display: flex;
    align-items: center;
    justify-content: center;
    gap: 10px;
    font-size: 27px;
    font-weight: 500;
    letter-spacing: 1px;
    color: var(--brand-ink);
    line-height: 1;
  }
  .brand-mark {
    width: 14px;
    height: 14px;
    background: var(--brand-ink);
  }
  .brand-web {
    margin-top: 20px;
    font-size: 14.5px;
    font-weight: 400;
    letter-spacing: 1.4px;
    color: var(--web-ink);
  }
  .card-heading {
    position: absolute;
    left: 290px;
    top: 100px;
    width: 468px;
    text-align: center;
  }
  .holder-name {
    margin: 0;
    font-size: 25px;
    font-weight: 500;
    letter-spacing: 1.3px;
    color: var(--name-ink);
    line-height: 1.2;
  }
  .holder-tagline {
    margin: 4px 0 0;
    font-size: 15px;
    font-weight: 400;
    letter-spacing: 0.8px;
    line-height: 18px;
    color: var(--tagline-ink);
    text-transform: uppercase;
  }
  .contact-list {
    position: absolute;
    left: 400px;
    top: 228px;
    margin: 0;
    padding: 0;
    list-style: none;
  }
  .contact-item {
    position: absolute;
    left: 0;
    display: flex;
    align-items: center;
    width: 340px;
  }
  .contact-item.address { top: 0; }
  .contact-item.phone { top: 60px; }
  .contact-item.email { top: 124px; }
  .contact-icon {
    width: 30px;
    display: flex;
    justify-content: center;
  }
  .contact-text {
    margin-left: 13px;
    padding-left: 8px;
    border-left: 1px solid var(--divider);
    font-size: 16px;
    line-height: 19px;
    letter-spacing: 0.3px;
    color: var(--contact-ink);
  }
</style>
</head>
<body>
<main class="canvas">
  <section class="business-card" aria-label="Business card for Daniel Whitford, CPA, PA">
    <svg class="card-shape" width="784" height="470" viewBox="0 0 784 470" aria-hidden="true">
      <defs>
        <radialGradient id="dark-panel" cx="0.58" cy="0.42" r="0.7">
          <stop offset="0" stop-color="var(--card-dark-center)"/>
          <stop offset="1" stop-color="var(--card-dark-edge)"/>
        </radialGradient>
      </defs>
      <path d="M196 0 Q300 235 196 470 L214 470 Q318 235 214 0 Z" fill="var(--curve-shade)"/>
      <path d="M206 0 Q306 235 206 470 L784 470 L784 0 Z" fill="url(#dark-panel)"/>
    </svg>

    <div class="brand-block">
      <div class="brand-name"><span class="brand-mark"></span>WHITFORD CPA</div>
      <div class="brand-web">WWW.WHITFORDCPA.COM</div>
    </div>

    <header class="card-heading">
      <h1 class="holder-name">DANIEL WHITFORD, CPA, PA</h1>
      <p class="holder-tagline">A Florida Profesional Asociation<br>Tax, Accounting &amp; Advisory Services</p>
    </header>

    <ul class="contact-list">
      <li class="contact-item address">
        <span class="contact-icon">
          <svg width="22" height="18" viewBox="0 0 22 18" aria-hidden="true">
            <path d="M11 1 L21 9 H18 V17 H13 V12 H9 V17 H4 V9 H1 Z" fill="#f0f0f3"/>
          </svg>
        </span>
        <span class="contact-text">240 Harbor View Ave.<br>Seaside Point, FL 32400</span>
      </li>
      <li class="contact-item phone">
        <span class="contact-icon">
          <svg width="24" height="24" viewBox="0 0 24 24" aria-hidden="true">
            <circle cx="12" cy="12" r="10.5" fill="none" stroke="#f0f0f3" stroke-width="1.5"/>
            <path d="M9.2 6.5 L10.6 9.2 L9.6 10.4 Q10.6 12.9 12.6 14.4 L13.8 13.4 L16.2 15 L15.2 16.9 Q11.4 17 8.6 12.4 Q7.2 9.2 9.2 6.5 Z" fill="#f0f0f3"/>
          </svg>
        </span>
        <span class="contact-text">(555)310-4827 office<br>(555)846-2190 mobile</span>
      </li>
      <li class="contact-item email">
        <span class="contact-icon">
          <svg width="22" height="15" viewBox="0 0 22 15" aria-hidden="true">
            <rect x="0.5" y="0.5" width="21" height="14" fill="#f0f0f3"/>
            <path d="M0.5 0.5 L11 8.5 L21.5 0.5" fill="none" stroke="#2a2c36" stroke-width="1.2"/>
          </svg>
        </span>
        <span class="contact-text" style="line-height:36px">dan@whitfordcpa.com</span>
      </li>
    </ul>
  </section>
</main>
</body>
</html>
```